Tavrel Crafted Interiors logo and business card

Tavrel is a female operated furniture design and reupholstery business. Working with luxury top end fabrics and furnishings for unique and stylish one off designs. Bringing loved pieces of furniture back to life by recovering on modern, trendy, stylish fabrics. Think Velvet chaise lounge or velour Chesterfield lounges, vibrant and unique colourful, individually designed statement pieces.
We would like a simple logo that can be used on socials and a business card that is simple yet striking . Possibly using a bronze or gold foil.
The business name is TAVREL CRAFTED INTERIORS
Can be just TAVREL
Logo will be used on socials and images of finished furniture.

Target Market(s)

high end luxury holiday houses. Artistic flair designer houses

Industry/Entity Type

Home Furniture

Contact Information for Business Card

Simple yet designer
Logo on the front and name details on the back

Font styles to use
Decorative

Requirements
Must have
• Finess
A feel of artistic design
Just a logo/business name on the front of the card
Should not have
• not a picture of furniture

```html
<!DOCTYPE html>
<html lang="en">
<head>
<meta charset="utf-8">
<title>Tavrel Crafted Interiors – Business Card</title>
<link href="https://fonts.googleapis.com/css2?family=Arimo:wght@400;700&family=Cinzel:wght@500;700&display=swap" rel="stylesheet">
<style>
  :root {
    --backdrop: #161616;
    --card-red: #f9393c;
    --card-white: #fcfcfc;
    --ink-light: #ffffff;
    --brand-red: #ee3235;
    --brand-charcoal: #333335;
  }
  * { margin: 0; padding: 0; box-sizing: border-box; }
  html, body {
    width: 1093px;
    height: 1200px;
    overflow: hidden;
    background: var(--backdrop);
    font-family: "Arimo", Arial, sans-serif;
  }
  .canvas {
    position: relative;
    width: 1093px;
    height: 1200px;
  }
  .card {
    position: absolute;
    left: 264px;
    height: 357px;
  }
  .card--back {
    top: 226px;
    width: 578px;
    background: var(--card-red);
    color: var(--ink-light);
    text-align: center;
  }
  .card--front {
    top: 620px;
    width: 582px;
    background: var(--card-white);
  }
  .holder-name {
    position: absolute;
    top: 69px;
    left: 0; right: 0;
    font-weight: 700;
    font-size: 22px;
    line-height: 1;
  }
  .holder-role {
    position: absolute;
    top: 91px;
    left: 0; right: 0;
    font-size: 17px;
    line-height: 1;
  }
  .rule {
    position: absolute;
    left: 218px;
    width: 142px;
    height: 1px;
    background: var(--ink-light);
  }
  .rule--upper { top: 121px; }
  .rule--lower { top: 230px; }
  .contact-list {
    position: absolute;
    top: 134px;
    left: 0; right: 0;
    list-style: none;
    font-size: 17px;
    line-height: 21px;
  }
  .contact-list b { font-weight: 700; }
  .address {
    position: absolute;
    top: 249px;
    left: 0; right: 0;
    font-style: normal;
    font-size: 17px;
    line-height: 21px;
  }
  .wordmark {
    position: absolute;
    top: 134px;
    left: 0; right: 0;
    text-align: center;
    font-family: "Cinzel", "Times New Roman", serif;
    line-height: 1;
  }
  .wordmark-name {
    display: block;
    color: var(--brand-red);
    font-weight: 700;
    font-size: 72px;
    letter-spacing: 4px;
    padding-left: 4px;
  }
  .wordmark-line {
    display: block;
    margin-top: 8px;
    color: var(--brand-charcoal);
    font-weight: 500;
    font-size: 24px;
    letter-spacing: 2.5px;
    padding-left: 2.5px;
  }
</style>
</head>
<body>
  <main class="canvas">
    <section class="card card--back" aria-label="Business card, details side">
      <h1 class="holder-name">ELSIE MARROW</h1>
      <p class="holder-role">Managing Director</p>
      <div class="rule rule--upper"></div>
      <ul class="contact-list">
        <li><b>P:</b> 021-480 735 162</li>
        <li><b>M:</b> 021-480 735 162</li>
        <li><b>E:</b> hello@tavrelinteriors.com</li>
        <li><b>W:</b> www.tavrelinteriors.com</li>
      </ul>
      <div class="rule rule--lower"></div>
      <address class="address">48 Larkspur Lane, Unit 3<br>Wellmere, 204817.</address>
    </section>

    <section class="card card--front" aria-label="Business card, brand side">
      <div class="wordmark">
        <span class="wordmark-name">TAVREL</span>
        <span class="wordmark-line">CRAFTED INTERIORS</span>
      </div>
    </section>
  </main>
</body>
</html>
```